BrivaTrek Freight Services Business cards

Would like a very unique design catchy but professional for business cards. Please use log provided.Marlon WellsCeo and Founder TransCon Logistix Solutions1-888-913-3225mwells@tlsolutionsus.comwww.bfservicesco.com

```html
<!DOCTYPE html>
<html lang="en">
<head>
<meta charset="utf-8">
<title>BrivaTrek Freight Services – Business Cards</title>
<link href="https://fonts.googleapis.com/css2?family=Montserrat:wght@500;600;700&display=swap" rel="stylesheet">
<style>
  :root {
    --stage: #ececec;
    --card-dark: #161616;
    --card-dark-edge: #0b0b0b;
    --card-light: #f4f4f4;
    --brand-blue: #1a6fbf;
    --brand-red: #e3262b;
    --ink: #4a4a4a;
    --ink-soft: #5a5a5a;
    --white: #ffffff;
    --ghost: rgba(255,255,255,0.07);
  }
  * { box-sizing: border-box; margin: 0; padding: 0; }
  html, body { width: 1200px; height: 1000px; overflow: hidden; }
  body {
    background: var(--stage);
    font-family: "Montserrat", sans-serif;
    position: relative;
  }
  .card {
    position: absolute;
    left: 263px;
    width: 674px;
    height: 384px;
    border-radius: 20px;
    overflow: hidden;
  }
  .card--front {
    top: 88px;
    background: radial-gradient(ellipse at 50% 40%, #262626 0%, var(--card-dark) 55%, var(--card-dark-edge) 100%);
  }
  .card--back {
    top: 526px;
    background: var(--card-light);
  }
  .ghost-mark {
    position: absolute;
    left: 248px;
    top: 0;
    width: 180px;
    height: 180px;
    background: var(--ghost);
  }
  .brand {
    position: absolute;
    display: flex;
    flex-direction: column;
    align-items: center;
  }
  .brand__square {
    width: 46px;
    height: 46px;
    background: var(--brand-blue);
    margin-bottom: 14px;
  }
  .brand__name {
    color: var(--brand-blue);
    font-weight: 700;
    text-transform: uppercase;
    letter-spacing: 1px;
    white-space: nowrap;
  }
  .brand__rule {
    width: 100%;
    height: 2px;
    margin-top: 8px;
    background: linear-gradient(90deg, transparent, var(--brand-red) 30%, var(--brand-red) 70%, transparent);
  }
  .card--front .brand {
    left: 0; right: 0;
    top: 130px;
  }
  .card--front .brand__name { font-size: 26px; }
  .card--front .brand__rule { width: 360px; }
  .front-url {
    position: absolute;
    left: 0; right: 0;
    top: 343px;
    text-align: center;
    color: var(--white);
    font-size: 16px;
    font-weight: 500;
    letter-spacing: 0.6px;
  }
  .card--back .brand {
    left: 34px;
    top: 50px;
    width: 256px;
  }
  .card--back .brand__square { width: 36px; height: 36px; margin-bottom: 12px; }
  .card--back .brand__name { font-size: 16px; letter-spacing: 0.5px; }
  .person {
    position: absolute;
    right: 37px;
    top: 154px;
    text-align: right;
  }
  .person__name {
    color: var(--brand-blue);
    font-size: 17px;
    font-weight: 600;
    letter-spacing: 0.6px;
  }
  .person__title {
    color: var(--ink);
    font-size: 12px;
    font-weight: 500;
    letter-spacing: 0.8px;
    margin-top: 1px;
  }
  .pointer {
    position: absolute;
    right: 0;
    top: 158px;
  }
  .company {
    position: absolute;
    left: 34px;
    top: 241px;
    color: var(--ink);
    font-size: 13px;
    font-weight: 700;
    letter-spacing: 0.5px;
  }
  .contacts {
    position: absolute;
    left: 34px;
    top: 268px;
    list-style: none;
  }
  .contacts li {
    display: flex;
    align-items: center;
    height: 26px;
    color: var(--ink-soft);
    font-size: 13px;
    font-weight: 500;
    letter-spacing: 0.4px;
  }
  .contacts li.phone { font-size: 15px; letter-spacing: 1px; }
  .contacts svg { width: 22px; height: 22px; margin-right: 10px; flex: none; }
</style>
</head>
<body>

<section class="card card--front">
  <div class="ghost-mark"></div>
  <div class="brand">
    <div class="brand__square"></div>
    <div class="brand__name">BrivaTrek Freight Services</div>
    <div class="brand__rule"></div>
  </div>
  <div class="front-url">WWW.BFSERVICESCO.COM</div>
</section>

<section class="card card--back">
  <div class="brand">
    <div class="brand__square"></div>
    <div class="brand__name">BrivaTrek Freight Services</div>
    <div class="brand__rule"></div>
  </div>

  <div class="person">
    <div class="person__name">DUSTIN HARROW</div>
    <div class="person__title">CEO AND FOUNDER</div>
  </div>
  <svg class="pointer" width="24" height="24" viewBox="0 0 24 24" aria-hidden="true">
    <polygon points="0,12 24,0 24,24" fill="var(--brand-blue)"/>
  </svg>

  <div class="company">BRIVATREK FREIGHT SERVICES</div>
  <ul class="contacts">
    <li class="phone">
      <svg viewBox="0 0 22 22" aria-hidden="true">
        <circle cx="11" cy="11" r="11" fill="var(--brand-blue)"/>
        <path d="M7.5 5.5l2 2.2-1.1 1.4c.7 1.6 2 2.9 3.5 3.6l1.4-1.1 2.2 2-1 1.9c-3.9-.4-7.6-4.1-8-8z" fill="#fff"/>
      </svg>
      1-888-472-6081
    </li>
    <li>
      <svg viewBox="0 0 22 22" aria-hidden="true">
        <circle cx="11" cy="11" r="11" fill="var(--brand-blue)"/>
        <rect x="5.5" y="7" width="11" height="8" rx="1" fill="#fff"/>
        <path d="M5.8 7.5L11 11.5l5.2-4" stroke="var(--brand-blue)" stroke-width="1.2" fill="none"/>
      </svg>
      DHARROW@BFSERVICESCO.COM
    </li>
    <li>
      <svg viewBox="0 0 22 22" aria-hidden="true">
        <circle cx="11" cy="11" r="11" fill="var(--brand-blue)"/>
        <circle cx="11" cy="11" r="6" fill="none" stroke="#fff" stroke-width="1.4"/>
        <ellipse cx="11" cy="11" rx="2.6" ry="6" fill="none" stroke="#fff" stroke-width="1.2"/>
        <line x1="5" y1="11" x2="17" y2="11" stroke="#fff" stroke-width="1.2"/>
      </svg>
      WWW.BFSERVICESCO.COM
    </li>
  </ul>
</section>

</body>
</html>
```